Chiropractic Office Needs a Poster for Cryotherapy

We are a chiropractic clinic that caters mostly to athletes. We've recently purchased the first whole body cryotherapy unit in San Antonio, TX (for commercial use - the SA Condors have a unit for their facility). We need a professional, attention grabbing poster created for patient education for our lobby area.
Updates

Poster size 20"X30" (horizontal)

our page link: www.facebook.com/mervalebackcare

Industry/Entity Type

Education

Requirements
Must have
• Image of the cryotherapy unit

"Schedule your appointment today"

"Like us on our page for Special Promos" (or something along those lines with FB button)

"www.mervalebackcare.example" & "210-555-0193"

"WHOLE BODY CRYOTHERAPY"

"Just 3 Minutes for Whole Body Recovery"

"How it works....
Inside the cryosauna, which is a tall, cylindrical chamber where the client stands, the body is surrounded by hyper-cooled air at an
average temperature of –220˚F for 2 ½ to 3 minutes. Cold sensors in the skin send a signal to the brain which causes blood to rush
to the core. As blood is circulated through the core, toxins are flushed and blood becomes enriched with oxygen and all the
necessary enzymes and nutrients."

"…Accelerate…
When the session ends, the oxygenated, nutrient and enzyme enriched blood rushes back through the body accelerating the natural recovery process. The release of endorphins, metabolic rate, and production of collagen are accelerated"

"…Recovery!
Recovery time is shortened, energy level is dramatically increased, and the endorphin release aids the body in dealing with pain and inflammation. The increase in metabolic rate allows the body to burn more calories and the production of collagen improves whole body skin elasticity and smoothness."

"BENEFITS INCLUDE:
Pain Management
Injury Therapy
Inflammatory Disorders
Rapid Recovery
Performance Enhancement
Metabolic & Immunity Boost
Anti-Aging
Skin Rejuvenation"
Nice to have
• Logo Attached below - we use the black & blue logo in the horizontal format

```html
<!DOCTYPE html>
<html lang="en">
<head>
<meta charset="utf-8">
<title>Whole Body Cryotherapy – Mervale Back Care</title>
<link rel="stylesheet" href="https://fonts.googleapis.com/css2?family=Orbitron:wght@800&family=Open+Sans:ital,wght@0,400;0,600;0,700;0,800;1,400&display=swap">
<style>
  :root {
    --ice: #dcefee;
    --ice-deep: #c6e3e3;
    --charcoal: #333333;
    --smoke: #3c3c3c;
    --title-blue: #52c3ee;
    --panel-blue: #5aaee0;
    --accent-blue: #2aa3e0;
    --ink: #2a2a2a;
    --ink-soft: #3a3a3a;
    --white: #ffffff;
    --footer-top: #f2f2f2;
    --footer-bottom: #c9c9c9;
  }
  * { margin: 0; padding: 0; box-sizing: border-box; }
  html, body { width: 1200px; height: 800px; overflow: hidden; }
  body { font-family: "Open Sans", Arial, sans-serif; color: var(--ink); }

  .poster {
    position: relative;
    width: 1200px;
    height: 800px;
    overflow: hidden;
    background: linear-gradient(180deg, var(--ice) 0%, #e6f3f2 60%, var(--ice-deep) 100%);
  }

  .title-block {
    position: absolute;
    left: 40px; top: 0;
    width: 460px; height: 133px;
    background: var(--charcoal);
    padding: 20px 0 0 42px;
  }
  .title-block h1 {
    font-family: "Orbitron", "Arial Black", sans-serif;
    font-weight: 800;
    color: var(--title-blue);
    font-size: 38px;
    line-height: 46px;
    letter-spacing: 1px;
    white-space: nowrap;
  }

  .tagline {
    position: absolute;
    left: 40px; top: 166px;
    font-size: 25px;
    font-style: italic;
    color: var(--ink-soft);
    letter-spacing: -0.3px;
    white-space: nowrap;
  }
  .tagline strong { font-weight: 800; }
  .tagline-swoosh { position: absolute; left: 84px; top: 196px; }

  .benefits-band {
    position: absolute;
    left: 0; top: 226px;
    width: 620px; height: 310px;
    background: linear-gradient(90deg, var(--smoke) 0%, #444 55%, rgba(80,80,80,0.6) 80%, rgba(220,239,238,0) 100%);
  }
  .benefits {
    position: absolute;
    left: 58px; top: 242px;
    color: var(--white);
  }
  .benefits h2 {
    font-size: 25px;
    font-weight: 700;
    margin-bottom: 11px;
    letter-spacing: 0.2px;
  }
  .benefits ul { list-style: none; }
  .benefits li {
    font-size: 20.5px;
    line-height: 28.5px;
    white-space: nowrap;
  }
  .benefits li::before {
    content: "+";
    font-weight: 700;
    margin-right: 14px;
  }

  .figure-art {
    position: absolute;
    left: 375px; top: 250px;
    width: 150px; height: 275px;
    border-radius: 70px;
    background: radial-gradient(ellipse at center, #f4fbfd 0%, #cfe9f2 40%, rgba(120,140,150,0) 72%);
  }

  .unit-art {
    position: absolute;
    left: 570px; top: 50px;
    width: 295px; height: 580px;
    border-radius: 14px;
    background: linear-gradient(90deg, #5d5f63 0%, #8d9094 35%, #6a6c70 65%, #44464a 100%);
  }

  .cta {
    position: absolute;
    text-align: center;
    color: var(--ink-soft);
  }
  .cta .small {
    font-size: 17px;
    letter-spacing: 2.4px;
    line-height: 22px;
  }
  .cta .big {
    font-size: 24px;
    font-weight: 800;
    line-height: 26px;
    letter-spacing: -0.2px;
    white-space: nowrap;
  }
  .cta .contact {
    font-size: 14.5px;
    line-height: 17px;
  }
  .cta-appointment { left: 45px; top: 554px; width: 200px; }
  .cta-appointment .contact { margin-top: 12px; }
  .cta-promos { left: 295px; top: 554px; width: 260px; }
  .cta-promos .contact { margin-top: 18px; font-size: 15px; }

  .info-panel {
    position: absolute;
    left: 897px; top: 0;
    width: 303px; height: 690px;
    background: var(--panel-blue);
    padding: 6px 28px 0 18px;
  }
  .info-panel h3 {
    color: var(--white);
    font-size: 26px;
    font-weight: 700;
    line-height: 30px;
    letter-spacing: 0.3px;
  }
  .info-panel p {
    color: var(--ink);
    font-size: 14px;
    line-height: 18.6px;
    padding-left: 20px;
    margin-bottom: 2px;
  }

  .footer {
    position: absolute;
    left: 0; top: 690px;
    width: 1200px; height: 110px;
    background: linear-gradient(180deg, var(--footer-top) 0%, var(--footer-bottom) 100%);
    display: flex;
    align-items: center;
    justify-content: center;
    gap: 16px;
  }
  .brand-mark {
    width: 34px; height: 34px;
    background: var(--accent-blue);
  }
  .brand-name {
    font-size: 30px;
    font-weight: 600;
    letter-spacing: 2px;
    color: var(--ink);
  }
</style>
</head>
<body>
<main class="poster">
  <header class="title-block">
    <h1>WHOLE BODY<br>CRYOTHERAPY</h1>
  </header>

  <p class="tagline">Just <strong>3 Minutes</strong> for Whole Body Recovery</p>
  <svg class="tagline-swoosh" width="120" height="10" viewBox="0 0 120 10" aria-hidden="true">
    <path d="M2 7 Q60 1 118 5" fill="none" stroke="var(--accent-blue)" stroke-width="3" stroke-linecap="round"/>
  </svg>

  <div class="benefits-band"></div>
  <section class="benefits">
    <h2>BENEFITS INCLUDE</h2>
    <ul>
      <li>Pain Management</li>
      <li>Injury Therapy</li>
      <li>Inflammatory Disorders</li>
      <li>Rapid Recovery</li>
      <li>Performance Enhancement</li>
      <li>Metabolic &amp; Immunity Boost</li>
      <li>Anti-Aging</li>
      <li>Skin Rejuvenation</li>
    </ul>
  </section>

  <div class="figure-art" role="img" aria-label="Glowing silhouette of a standing human body"></div>

  <div class="unit-art" role="img" aria-label="Photo of the whole body cryotherapy chamber with cold vapour rising"></div>

  <section class="cta cta-appointment">
    <p class="small">schedule your</p>
    <p class="big">APPOINTMENT</p>
    <p class="small">today</p>
    <p class="contact">210-555-0193<br>www.mervalebackcare.example</p>
  </section>

  <section class="cta cta-promos">
    <p class="small">Keep up with our</p>
    <p class="big">SPECIAL PROMOS</p>
    <p class="small">on our page</p>
    <p class="contact">mervalebackcare.example/promos</p>
  </section>

  <aside class="info-panel">
    <h3>How it works</h3>
    <p>Inside the cryosauna, which is a tall, cylindrical chamber where the client stands, the body is surrounded by hyper-cooled air at an average temperature of –220˚F for 2 ½ to 3 minutes. Cold sensors in the skin send a signal to the brain which causes blood to rush to the core. As blood is circulated through the core, toxins are flushed and blood becomes enriched with oxygen and all the necessary enzymes and nutrients.</p>
    <h3>Accelerate</h3>
    <p>When the session ends, the oxygenated, nutrient and enzyme enriched blood rushes back through the body accelerating the natural recovery process. The release of endorphins, metabolic rate, and production of collagen are accelerated</p>
    <h3>Recovery!</h3>
    <p>Recovery time is shortened, energy level is dramatically increased, and the endorphin release aids the body in dealing with pain and inflammation. The increase in metabolic rate allows the body to burn more calories and the production of collagen improves whole body skin elasticity and smoothness.</p>
  </aside>

  <footer class="footer">
    <span class="brand-mark" aria-hidden="true"></span>
    <span class="brand-name">MERVALE BACK CARE</span>
  </footer>
</main>
</body>
</html>
```